Tights Color Chart

We Need for a Webshop 3 or 4 different Color Charts to see the Colors of the Tights.

1 Color Chart only with this Colors: black/schwarz, white/weiss,
naturel/natur.

The other 3 or 4 Charts up to your Design!

Total 54 Colors.

The Language must be in English and German.
Each single Color Chart should have rounded Corners see attachment.

Thank you in advance
BEN

Target Market(s)

Woman, Webshop

Requirements
Must have
• the right Colors, English and German, for the Webshop

```html
<!DOCTYPE html>
<html lang="en">
<head>
<meta charset="utf-8">
<title>Tights Color Chart</title>
<link href="https://fonts.googleapis.com/css2?family=Noto+Sans:wght@400&display=swap" rel="stylesheet">
<style>
:root{
  --bg:#ffffff;
  --ink:#333333;
  --edge:#e6e6e6;
  --black:#474545;--white:#ffffff;--naturel:#c79f87;
  --cream:#fefff0;--kalina:#fafafa;--ecru:#f8f8f6;--perle:#f2f2ea;--ash:#dfdfe0;--cacao:#9b7d78;--nugat:#84645b;--bronzo:#5e4446;--beige:#ad8468;--orange:#e49342;--salmon:#f4a79d;--rose:#f8e4e9;--babypink:#fdf0f4;
  --rosso:#bd4f4b;--lipstic:#ad4b55;--sorbet:#d94f5d;--raspberry:#e05577;--orchidea:#f399c6;--pink:#f194c2;--crocus:#d653a1;--lavende:#c66390;--fuchsia:#a54779;--mulberry:#93496d;--violet:#8d3d67;--prugna:#8e5973;--berry:#7a5870;
  --olive:#5a5d41;--kiwi:#e5fb9d;--verde:#87da87;--grass:#47aa5e;--aquamarina:#a9edd6;--lagoon:#2fc6ba;--lazur:#66d8d5;--turquoise:#34ccd4;--blue:#62b3dd;--babyblue:#b6d1ed;--lilla:#b9a3cf;--iris:#9069b0;--azalea:#8e5699;
  --jeans:#64618f;--ocean:#50738a;--night:#474259;--blumarino:#4a3759;--bmmelange:#5c4c70;--denim:#3e3641;--silver:#60666a;--steel:#7a6a74;--gray:#604f5a;--graphite:#54494a;--smoke:#535257;--nero:#514d4e;
}
*{margin:0;padding:0;box-sizing:border-box}
html,body{width:1200px;height:1020px;overflow:hidden;background:var(--bg)}
body{font-family:"Noto Sans",sans-serif;color:var(--ink);position:relative}
.chart{position:absolute;left:83px;display:grid;grid-auto-flow:column}
.chart--basics{top:83px;grid-template-columns:repeat(3,106px)}
.chart--row{grid-template-columns:repeat(13,81.25px)}
.chart--r1{top:258px}.chart--r2{top:433px}.chart--r3{top:608px}.chart--r4{top:783px}
.color{display:flex;align-items:flex-end;height:150px}
.swatch{width:41.7px;height:150px;border-radius:7px;flex:none}
.chart--basics .swatch{width:66.7px}
.swatch--light{border:1px solid var(--edge)}
.label{writing-mode:vertical-rl;transform:rotate(180deg);font-size:10px;line-height:10px;max-height:150px;margin-left:4px;white-space:normal}
</style>
</head>
<body>
<section class="chart chart--basics">
  <div class="color"><div class="swatch" style="background:var(--black)"></div><span class="label">black • schwarz</span></div>
  <div class="color"><div class="swatch swatch--light" style="background:var(--white)"></div><span class="label">white • weiss</span></div>
  <div class="color"><div class="swatch" style="background:var(--naturel)"></div><span class="label">naturel • natur</span></div>
</section>

<section class="chart chart--row chart--r1">
  <div class="color"><div class="swatch swatch--light" style="background:var(--cream)"></div><span class="label">cream • creme</span></div>
  <div class="color"><div class="swatch swatch--light" style="background:var(--kalina)"></div><span class="label">kalina • kalina</span></div>
  <div class="color"><div class="swatch" style="background:var(--ecru)"></div><span class="label">ecru • ecru</span></div>
  <div class="color"><div class="swatch" style="background:var(--perle)"></div><span class="label">perle • perle</span></div>
  <div class="color"><div class="swatch" style="background:var(--ash)"></div><span class="label">ash • asche</span></div>
  <div class="color"><div class="swatch" style="background:var(--cacao)"></div><span class="label">cacao • kakao</span></div>
  <div class="color"><div class="swatch" style="background:var(--nugat)"></div><span class="label">nugat • nougat</span></div>
  <div class="color"><div class="swatch" style="background:var(--bronzo)"></div><span class="label">bronzo • bronze</span></div>
  <div class="color"><div class="swatch" style="background:var(--beige)"></div><span class="label">beige • beige</span></div>
  <div class="color"><div class="swatch" style="background:var(--orange)"></div><span class="label">orange • orange</span></div>
  <div class="color"><div class="swatch" style="background:var(--salmon)"></div><span class="label">salmon • lachs</span></div>
  <div class="color"><div class="swatch" style="background:var(--rose)"></div><span class="label">rose • hellrosa</span></div>
  <div class="color"><div class="swatch" style="background:var(--babypink)"></div><span class="label">baby pink • baby rosa</span></div>
</section>

<section class="chart chart--row chart--r2">
  <div class="color"><div class="swatch" style="background:var(--rosso)"></div><span class="label">rosso • rosso</span></div>
  <div class="color"><div class="swatch" style="background:var(--lipstic)"></div><span class="label">lipstic • rot</span></div>
  <div class="color"><div class="swatch" style="background:var(--sorbet)"></div><span class="label">sorbet • sorbet</span></div>
  <div class="color"><div class="swatch" style="background:var(--raspberry)"></div><span class="label">raspberry • himbeere</span></div>
  <div class="color"><div class="swatch" style="background:var(--orchidea)"></div><span class="label">orchidea • orchidea</span></div>
  <div class="color"><div class="swatch" style="background:var(--pink)"></div><span class="label">pink • rosa</span></div>
  <div class="color"><div class="swatch" style="background:var(--crocus)"></div><span class="label">crocus • krokus</span></div>
  <div class="color"><div class="swatch" style="background:var(--lavende)"></div><span class="label">lavende • lavendel</span></div>
  <div class="color"><div class="swatch" style="background:var(--fuchsia)"></div><span class="label">fuchsia • fuchsia</span></div>
  <div class="color"><div class="swatch" style="background:var(--mulberry)"></div><span class="label">mulberry • maulbeere</span></div>
  <div class="color"><div class="swatch" style="background:var(--violet)"></div><span class="label">violet • violett</span></div>
  <div class="color"><div class="swatch" style="background:var(--prugna)"></div><span class="label">prugna • pflaume</span></div>
  <div class="color"><div class="swatch" style="background:var(--berry)"></div><span class="label">berry • beeren</span></div>
</section>

<section class="chart chart--row chart--r3">
  <div class="color"><div class="swatch" style="background:var(--olive)"></div><span class="label">olive • olive</span></div>
  <div class="color"><div class="swatch" style="background:var(--kiwi)"></div><span class="label">kiwi • kiwi</span></div>
  <div class="color"><div class="swatch" style="background:var(--verde)"></div><span class="label">verde • grün</span></div>
  <div class="color"><div class="swatch" style="background:var(--grass)"></div><span class="label">grass • grassgrün</span></div>
  <div class="color"><div class="swatch" style="background:var(--aquamarina)"></div><span class="label">aquamarina • aquamarin</span></div>
  <div class="color"><div class="swatch" style="background:var(--lagoon)"></div><span class="label">lagoon • lagune</span></div>
  <div class="color"><div class="swatch" style="background:var(--lazur)"></div><span class="label">lazur • lazur</span></div>
  <div class="color"><div class="swatch" style="background:var(--turquoise)"></div><span class="label">turquoise • türkis</span></div>
  <div class="color"><div class="swatch" style="background:var(--blue)"></div><span class="label">blue • blau</span></div>
  <div class="color"><div class="swatch" style="background:var(--babyblue)"></div><span class="label">baby blue • baby blau</span></div>
  <div class="color"><div class="swatch" style="background:var(--lilla)"></div><span class="label">lilla • lila</span></div>
  <div class="color"><div class="swatch" style="background:var(--iris)"></div><span class="label">iris • iris</span></div>
  <div class="color"><div class="swatch" style="background:var(--azalea)"></div><span class="label">azalea • azalee</span></div>
</section>

<section class="chart chart--row chart--r4">
  <div class="color"><div class="swatch" style="background:var(--jeans)"></div><span class="label">jeans • jeans</span></div>
  <div class="color"><div class="swatch" style="background:var(--ocean)"></div><span class="label">ocean • ozean</span></div>
  <div class="color"><div class="swatch" style="background:var(--night)"></div><span class="label">night • nacht</span></div>
  <div class="color"><div class="swatch" style="background:var(--blumarino)"></div><span class="label">blu marino • blu marino</span></div>
  <div class="color"><div class="swatch" style="background:var(--bmmelange)"></div><span class="label">blu marino melange • blu marino melange</span></div>
  <div class="color"><div class="swatch" style="background:var(--denim)"></div><span class="label">denim • denim</span></div>
  <div class="color"><div class="swatch" style="background:var(--silver)"></div><span class="label">silver • silber</span></div>
  <div class="color"><div class="swatch" style="background:var(--steel)"></div><span class="label">steel • stehlen</span></div>
  <div class="color"><div class="swatch" style="background:var(--gray)"></div><span class="label">gray • grau</span></div>
  <div class="color"><div class="swatch" style="background:var(--graphite)"></div><span class="label">graphite • graphit</span></div>
  <div class="color"><div class="swatch" style="background:var(--smoke)"></div><span class="label">smoke • rauch</span></div>
  <div class="color"><div class="swatch" style="background:var(--nero)"></div><span class="label">nero melange • schwarz melange</span></div>
</section>
</body>
</html>
```